Whimsical Business Card Design

We would like a fun and whimsically designed business card. We are a business out of British Columbia and we make creatively designed soaps, shampoo, conditioner, body lotion, massage oil, and essential oil blends mainly for women. We use all natural ingredients scented with essential oils. I would like the design to be girlie, fun, whimsical with character drawings of a shorter white haired lady (my mother) typical short (5'5") grey haired adorable classy granny with dainty pearl earings, and a younger lady (me) taller (5'8") with shoulder length brown layered hair that flips up in the layers (been told I look similar to Dana Whitlock - modern drop earrings. We can be throwing bubbles, holding each other with one arm and displaying our swirled designer soap in the other hand with bubbles floating, or blowing bubbles at each other, with or without an apron, looking like we are having fun! We are both practical jokers and love to have a good time. This business is very fun! . My favourite colours are teal, bluegreen, ocean blue, pink, lime green for fun colours. If you have a better design in mind I am open. Thanks team!cards I like ID: ID 7390562 - whimsicalID: 8574031 (brown dot) like the colours and character drawing

Target Market(s)

Younger to middle aged

Industry/Entity Type

Skin Care Product

Contact Information for Business Card

Pippa & Fizz
Bath & Body Essentials
Marnie Holt
Fernbrook Bay
604-287-3918

Font styles to use
Decorative

Colors
acd036
33a6d7
fbed22
e667a6

Requirements
Must have
• Fun and whimsical theme
Nice to have
• I would like the design to be girlie, fun, whimsical with character drawings of a shorter white haired lady (my mother) typical short (5'5") grey haired adorable classy granny with dainty pearl earings, and a younger lady (me) taller (5'8") with shoulder length brown layered hair that flips up in the layers (been told I look similar to Dana Whitlock - modern drop earrings. We can be throwing bubbles, holding each other with one arm and displaying our swirled designer soap in the other hand with bubbles floating, or blowing bubbles at each other, with or without an apron, looking like we are having fun! We are both practical jokers and love to have a good time. This business is very fun! . My favourite colours are teal, bluegreen, ocean blue, pink, lime green for fun colours. If you have a better design in mind I am open. Thanks team!cards I like ID: ID 7390562 - whimsicalID: 8574031 (brown dot) like the colours and character drawing

```html
<!DOCTYPE html>
<html lang="en">
<head>
<meta charset="utf-8">
<title>Pippa &amp; Fizz – Business Card</title>
<link rel="stylesheet" href="https://fonts.googleapis.com/css2?family=Open+Sans:wght@400;600&display=swap">
<style>
  :root {
    --stage: #2c2d31;
    --card-white: #ffffff;
    --card-mist: #eceef4;
    --ocean: #33a6d7;
    --ocean-deep: #1f8fcf;
    --ocean-light: #5cc0ea;
    --pink: #e667a6;
    --lime: #acd036;
    --sun: #fbed22;
    --ink-light: #ffffff;
    --ink-soft: #6f7c8c;
  }
  * { box-sizing: border-box; margin: 0; padding: 0; }
  html, body {
    width: 1200px; height: 900px; overflow: hidden;
    background: var(--stage);
  }
  .business-card {
    position: absolute; left: 100px; top: 164px;
    width: 1000px; height: 572px;
    background: radial-gradient(circle at 30% 70%, var(--card-white) 0%, var(--card-mist) 75%);
    box-shadow: 0 18px 40px rgba(0,0,0,.45);
    overflow: hidden;
    font-family: "Open Sans", sans-serif;
  }
  .contact-panel {
    position: absolute; left: 520px; top: 40px;
    width: 480px; height: 300px;
    background: linear-gradient(135deg, var(--ocean-deep) 0%, var(--ocean) 55%, var(--ocean-light) 100%);
    color: var(--ink-light);
    padding: 58px 0 0 66px;
  }
  .contact-name { font-size: 31px; font-weight: 600; }
  .contact-list { list-style: none; margin-top: 54px; font-size: 21px; line-height: 32px; }
  .contact-list li { display: flex; align-items: center; gap: 12px; }
  .contact-icon { width: 22px; height: 20px; flex: none; }
  .brand-art {
    position: absolute; left: 110px; top: 180px;
    width: 350px; height: 190px;
    border-radius: 14px;
    background: linear-gradient(120deg, var(--ocean-light) 0%, var(--lime) 40%, var(--pink) 70%, var(--sun) 100%);
    opacity: .55;
  }
  .brand-name {
    position: absolute; left: 110px; top: 392px;
    font-weight: 600; font-size: 44px; line-height: 56px;
    color: var(--ocean);
  }
  .brand-tagline {
    position: absolute; left: 112px; top: 458px;
    font-weight: 400; font-size: 18px; letter-spacing: 1px;
    color: var(--ink-soft);
  }
</style>
</head>
<body>
  <article class="business-card">
    <div class="brand-art" role="img" aria-label="Illustration of two smiling women, one holding a swirled soap, with blue bubbles floating around them"></div>
    <div class="brand-name">Pippa &amp; Fizz</div>
    <div class="brand-tagline">Bath and Body Essentials</div>

    <section class="contact-panel">
      <h1 class="contact-name">Marnie Holt</h1>
      <ul class="contact-list">
        <li>Fernbrook Bay</li>
        <li>
          <svg class="contact-icon" viewBox="0 0 22 20" aria-hidden="true">
            <rect x="1" y="1" width="20" height="18" fill="none" stroke="#fff" stroke-width="2"/>
            <path d="M6 6c0 5 5 9 10 9l1-3-3-1-1 1c-2-1-3-2-4-4l1-1-1-3z" fill="#fff"/>
          </svg>
          604-287-3918
        </li>
        <li>
          <svg class="contact-icon" viewBox="0 0 22 20" aria-hidden="true">
            <rect x="1" y="1" width="20" height="18" fill="none" stroke="#fff" stroke-width="2"/>
            <path d="M4 5h14v10H4z M4 5l7 6 7-6" fill="none" stroke="#fff" stroke-width="1.6"/>
          </svg>
          hello@pippafizz.ca
        </li>
      </ul>
    </section>
  </article>
</body>
</html>
```